Design business card two side.
Simple and modern design like:

https://media.plovarkit.net/wp-content/uploads/2016/09/12062906/Modern-Design-Business-Card-Template.jpg
https://k7.zubrimo.net/jpg/01/84/37/46/500_F_184374698_YLFWErxqrO1rgFAP7l9cvpWwpbOhgdU5.jpg
https://www.quennoberhive.com/wp-content/uploads/2017/04/Modern-Business-Card-Design-Template-5.jpg
http://wtx.morvelanthopaxis.com/wp-content/uploads/2013/03/modern+business+cards+13.jpg

Logo can be found in two types.

```html
<!DOCTYPE html>
<html lang="en">
<head>
<meta charset="utf-8">
<title>Rovanta business card</title>
<link rel="stylesheet" href="https://fonts.googleapis.com/css2?family=Open+Sans:wght@400;600&family=Tinos&display=swap">
<style>
  :root {
    --backdrop: #2b2b2d;
    --blue-light: #5cc6ee;
    --blue-mid: #34a8df;
    --blue-deep: #1f8fd1;
    --band: #f1dfe5;
    --white: #ffffff;
    --ink: #1b2a3a;
    --icon-bg: #eef3f7;
  }
  * { margin: 0; padding: 0; box-sizing: border-box; }
  html, body { width: 1200px; height: 911px; overflow: hidden; }
  body {
    background: var(--backdrop);
    display: flex;
    align-items: center;
    justify-content: center;
    gap: 70px;
    font-family: "Open Sans", sans-serif;
  }
  .card {
    position: relative;
    width: 440px;
    height: 770px;
    overflow: hidden;
    background: linear-gradient(160deg, var(--blue-light) 0%, var(--blue-mid) 45%, var(--blue-deep) 100%);
  }
  .card-front .band {
    position: absolute;
    left: -40px;
    top: 330px;
    width: 520px;
    height: 46px;
    background: var(--band);
    transform: rotate(-8deg);
  }
  .card-front .band-shade {
    position: absolute;
    left: -40px;
    top: 352px;
    width: 520px;
    height: 40px;
    background: var(--blue-light);
    opacity: .55;
    transform: rotate(-8deg);
  }
  .brand {
    position: absolute;
    display: flex;
    align-items: center;
    gap: 16px;
    color: var(--white);
    font-weight: 600;
  }
  .brand-mark { background: var(--white); flex: none; }
  .card-front .brand { left: 50px; top: 150px; font-size: 58px; }
  .card-front .brand-mark { width: 26px; height: 26px; }
  .holder { position: absolute; left: 50px; top: 450px; color: var(--white); }
  .holder-name { font-size: 30px; letter-spacing: 1px; font-weight: 400; }
  .holder-role { font-size: 17px; margin-top: 2px; }
  .holder-rule { width: 190px; height: 2px; background: var(--white); margin-top: 14px; }
  .contacts { position: absolute; left: 50px; top: 585px; list-style: none; color: var(--white); font-size: 16px; }
  .contacts li { display: flex; align-items: center; gap: 16px; margin-bottom: 16px; line-height: 1.35; }
  .contacts svg { width: 36px; height: 36px; flex: none; }
  .card-back .brand { left: 50%; top: 300px; transform: translateX(-50%); font-size: 82px; }
  .card-back .brand-mark { width: 34px; height: 34px; }
  .card-back .address {
    position: absolute;
    left: 0; right: 0;
    top: 430px;
    text-align: center;
    font-family: "Tinos", serif;
    font-size: 22px;
    color: var(--ink);
  }
</style>
</head>
<body>
  <section class="card card-front">
    <div class="band-shade"></div>
    <div class="band"></div>
    <div class="brand"><span class="brand-mark"></span>Rovanta</div>
    <div class="holder">
      <div class="holder-name">MAREK ODELL</div>
      <div class="holder-role">Designer</div>
      <div class="holder-rule"></div>
    </div>
    <ul class="contacts">
      <li>
        <svg viewBox="0 0 36 36" aria-hidden="true"><circle cx="18" cy="18" r="17" fill="var(--icon-bg)"/><path d="M13 10c1.5 0 3 3.5 3 4.5s-1.5 1.5-1.5 2.5 3 5 4.5 5 1.5-1.5 2.5-1.5 4.5 1.5 4.5 3-2 3-4 3c-5 0-12-7-12-12 0-2 1.5-4.5 3-4.5z" fill="var(--ink)"/></svg>
        +00 555 019 2746
      </li>
      <li>
        <svg viewBox="0 0 36 36" aria-hidden="true"><circle cx="18" cy="18" r="17" fill="var(--icon-bg)"/><rect x="9" y="12" width="18" height="13" rx="1.5" fill="none" stroke="var(--ink)" stroke-width="2"/><path d="M9.5 13l8.5 7 8.5-7" fill="none" stroke="var(--ink)" stroke-width="2"/></svg>
        marek@rovanta-mail.com
      </li>
      <li>
        <svg viewBox="0 0 36 36" aria-hidden="true"><circle cx="18" cy="18" r="17" fill="var(--icon-bg)"/><path d="M18 8a7 7 0 0 1 7 7c0 5-7 13-7 13s-7-8-7-13a7 7 0 0 1 7-7z" fill="var(--ink)"/><circle cx="18" cy="15" r="2.6" fill="var(--icon-bg)"/></svg>
        <span>88, 3rd Floor<br>Linden Lane, Brm-2260</span>
      </li>
    </ul>
  </section>

  <section class="card card-back">
    <div class="brand"><span class="brand-mark"></span>Rovanta</div>
    <p class="address">Harlow Bay, Westmere-2260</p>
  </section>
</body>
</html>
```